Postcard Design

business name: COZY HOUR KEEPER. I am a mother of 2 well adjusted, successful teenage boys. I decided to start this company caring for kids who are home sick, unable to go to daycare or school, and when their parent cant stay home with them. I was also a career woman for many years, with no friends available or family nearby to help when i was in an emergency situation for childcare. I know how stressful it can be when a child gets sick suddenly and unexpectedly. I would like to help out those parents in need, that have pressing schedules and a sick child at home that they really want to take care of, but cant due to their work pressures and priorities. I want parents to know that their child is safe and I can help them when in need, at last minute. The design should show the child is safe and well cared for and the parent is at ease, able to accomplish their obligations. I have also founded a nonprofit environmental education program in which I teach children in youth summer camps. I have taught creativity arts combined with science curriculum in kindergarten to 8th grade non-formal teaching for the past 5 years. This is a small community, and many people know me. I will be handing out these postcards to local daycares and people I know.

Industry/Entity Type

Business

```html
<!DOCTYPE html>
<html lang="en">
<head>
<meta charset="utf-8">
<title>Cozy Hour Keeper Postcard</title>
<link rel="stylesheet" href="https://fonts.googleapis.com/css2?family=Roboto+Condensed:wght@700&family=Roboto:wght@300&family=Lato:wght@400;700&display=swap">
<style>
  :root {
    --blue: #2f56a8;
    --blue-deep: #223f8c;
    --orange: #f7941d;
    --orange-light: #ffc93c;
    --pink: #ec2a8c;
    --green: #7cc242;
    --lime: #a6d84a;
    --yellow: #ffd838;
    --ink: #231f20;
    --white: #ffffff;
  }
  * { margin: 0; padding: 0; box-sizing: border-box; }
  html, body { width: 1200px; height: 982px; overflow: hidden; background: #f2f2f2; }
  .postcard { position: relative; width: 1200px; height: 982px; overflow: hidden; font-family: "Lato", sans-serif; }
  .postcard-art { position: absolute; inset: 0; }
  .experience-years { position: absolute; left: 40px; top: 38px; color: var(--yellow); font: 700 40px/1 "Roboto Condensed", sans-serif; letter-spacing: 1px; }
  .experience-label { position: absolute; left: 40px; top: 92px; color: var(--white); font: 700 31px/1 "Roboto Condensed", sans-serif; letter-spacing: 0.5px; }
  .headline { position: absolute; left: 40px; top: 260px; }
  .headline-strong { display: block; color: var(--ink); font: 700 84px/1 "Roboto Condensed", sans-serif; letter-spacing: 1px; }
  .headline-light { display: block; color: var(--white); font: 300 86px/1.05 "Roboto", sans-serif; letter-spacing: 1px; }
  .intro { position: absolute; left: 42px; top: 472px; width: 445px; color: var(--ink); font-size: 25px; line-height: 35px; text-align: justify; hyphens: auto; }
  .badge-text { position: absolute; left: 744px; top: 566px; width: 220px; text-align: center; font: 700 36px/1.3 "Roboto Condensed", sans-serif; }
  .badge-text .accent { color: var(--pink); }
  .badge-text .main { color: var(--ink); font-size: 40px; }
  .contact-bar { position: absolute; left: 42px; right: 30px; top: 890px; display: flex; align-items: baseline; color: var(--white); white-space: nowrap; }
  .contact-name { font-weight: 700; font-size: 29px; margin-right: 30px; }
  .contact-call { font-weight: 700; font-size: 40px; color: var(--yellow); }
  .contact-phone { font-weight: 700; font-size: 40px; margin-right: 30px; }
  .contact-web { font-weight: 700; font-size: 29px; display: flex; align-items: center; gap: 10px; }
  .web-dot { width: 13px; height: 13px; border-radius: 50%; background: var(--orange-light); display: inline-block; }
</style>
</head>
<body>
<main class="postcard">
  <svg class="postcard-art" viewBox="0 0 1200 982" width="1200" height="982" aria-hidden="false">
    <defs>
      <radialGradient id="sunburst" cx="0.65" cy="0.55" r="0.7">
        <stop offset="0" stop-color="var(--orange-light)"/>
        <stop offset="0.55" stop-color="#fbb03b"/>
        <stop offset="1" stop-color="var(--orange)"/>
      </radialGradient>
      <linearGradient id="band" x1="0" y1="0" x2="1" y2="0">
        <stop offset="0" stop-color="var(--blue-deep)"/>
        <stop offset="1" stop-color="var(--blue)"/>
      </linearGradient>
      <linearGradient id="photoTone" x1="0" y1="0" x2="1" y2="1">
        <stop offset="0" stop-color="#e9d8b8"/>
        <stop offset="0.5" stop-color="#c9a27a"/>
        <stop offset="1" stop-color="#efe6d8"/>
      </linearGradient>
    </defs>

    <rect class="field" width="1200" height="982" fill="url(#sunburst)"/>

    <!-- top band -->
    <path class="top-band" d="M0 0 H640 L560 160 Q320 175 0 228 Z" fill="url(#band)"/>
    <path class="top-line-green" d="M0 236 Q320 182 560 168" stroke="var(--green)" stroke-width="9" fill="none"/>
    <path class="top-line-pink" d="M0 250 Q320 196 560 182" stroke="var(--pink)" stroke-width="7" fill="none"/>

    <!-- photo circle rings -->
    <path class="lower-arc-green" d="M700 640 Q950 600 1200 560" stroke="var(--green)" stroke-width="10" fill="none"/>
    <path class="lower-arc-pink" d="M720 660 Q960 620 1200 582" stroke="var(--pink)" stroke-width="7" fill="none"/>
    <circle class="ring-pink" cx="915" cy="195" r="408" fill="var(--pink)"/>
    <circle class="ring-white" cx="915" cy="195" r="398" fill="var(--white)"/>
    <circle class="ring-green" cx="915" cy="195" r="390" fill="var(--green)"/>
    <circle class="photo-slot" cx="915" cy="195" r="376" fill="url(#photoTone)" role="img" aria-label="Photo of a caregiver gently checking a sick child's temperature as the child rests in bed under a blanket"/>

    <!-- bottom band -->
    <path class="bottom-line-green" d="M0 846 Q600 770 1200 840" stroke="var(--green)" stroke-width="10" fill="none"/>
    <path class="bottom-line-pink" d="M0 832 Q600 756 1200 826" stroke="var(--pink)" stroke-width="7" fill="none"/>
    <path class="bottom-band" d="M0 858 Q600 782 1200 852 V982 H0 Z" fill="url(#band)"/>

    <!-- scalloped badge -->
    <g class="badge" fill="var(--lime)" stroke="var(--white)" stroke-width="5">
      <g stroke="none" fill="var(--white)">
        <circle cx="854" cy="498" r="36"/><circle cx="930" cy="520" r="36"/><circle cx="972" cy="582" r="36"/>
        <circle cx="972" cy="662" r="36"/><circle cx="930" cy="724" r="36"/><circle cx="854" cy="746" r="36"/>
        <circle cx="778" cy="724" r="36"/><circle cx="736" cy="662" r="36"/><circle cx="736" cy="582" r="36"/>
        <circle cx="778" cy="520" r="36"/>
      </g>
      <g stroke="none">
        <circle cx="854" cy="502" r="31"/><circle cx="927" cy="523" r="31"/><circle cx="968" cy="584" r="31"/>
        <circle cx="968" cy="660" r="31"/><circle cx="927" cy="721" r="31"/><circle cx="854" cy="742" r="31"/>
        <circle cx="781" cy="721" r="31"/><circle cx="740" cy="660" r="31"/><circle cx="740" cy="584" r="31"/>
        <circle cx="781" cy="523" r="31"/>
        <circle cx="854" cy="622" r="118"/>
      </g>
    </g>
  </svg>

  <p class="experience-years">OVER 14 YEARS</p>
  <p class="experience-label">CHILD CARE EXPERIENCE</p>

  <h1 class="headline">
    <span class="headline-strong">COZY HOUR</span>
    <span class="headline-light">KEEPER</span>
  </h1>

  <p class="intro">I know how stressful it can be when a child gets sick suddenly and unexpectedly. I would like to help out those parents in need, that have pressing schedules and a sick child at home that they really want to take care of, but cant due to their work pressures and priorities.</p>

  <p class="badge-text">
    <span class="accent">5 years of</span><br>
    <span class="main">Teaching</span><br>
    <span class="accent">Experience</span>
  </p>

  <footer class="contact-bar">
    <span class="contact-name">Mara Lindell</span>
    <span class="contact-call">call now&nbsp;</span>
    <span class="contact-phone">-(555) 014-2290</span>
    <span class="contact-web"><span class="web-dot"></span>www.carelist.example/maral/cc</span>
  </footer>
</main>
</body>
</html>
```